Flyer für Natur- und Chiropraxis
Zielgruppe
Natur- und Chiropraxis. (Berufsbild Heilpraktiker)
Ganzheitliche Chiropraktik und manuelle Gelenktherapie.
Patienten mit chronischen oder akuten Beschwerden des Halte- und Bewegungsapparates (z.b. Migräne+Spannungskopfschmerzen, Muskelkettendysbalancen, Bandscheibenvorfälle)
HWS und Atlastherapie (Bei Tinnitus, Schwindel, Kopfschmerzen)
Naturheilkunde und Vitalstoffinfusionen (Bei LongCovid und chronischem Erschöpfungssyndrom)
Extrakorporale Stoßwellentherapie ( Bei Fersensporn, Kalkschulter, Sehnenansatzentzündungen.)
Nebensächlich=Neuraltherapie, Extensionstherapie, Wärmetherapie, Magnetfeldtherapie, biologische Arthrosebehandlung, Dry-Needling Therapie.
Aufgabenstellung
Bitte das Heilmittelwerbegesetz beachten!
Geplanter start der Praxis 17.04.23
Adresse der Praxis= Lindenweg 7, 57312 Kirchen. Tel. 02741/73945

```html
<!DOCTYPE html>
<html lang="de">
<head>
<meta charset="utf-8">
<title>Flyer Natur- und Chiropraxis</title>
<link href="https://fonts.googleapis.com/css2?family=Montserrat:wght@400;500;600;700&family=Nunito:wght@400;600;700&display=swap" rel="stylesheet">
<style>
:root{
  --bg:#e4e4e4;
  --panel:#8a8a8a;
  --panel-mid:#7b7b7b;
  --panel-dark:#6a6a6a;
  --ink-light:#ffffff;
  --accent-green:#8fdc7a;
  --footer:#f6f6f6;
  --footer-ink:#555;
}
*{box-sizing:border-box;margin:0;padding:0}
html,body{width:1200px;height:900px;overflow:hidden}
body{background:var(--bg);font-family:"Montserrat",sans-serif;color:var(--ink-light);position:relative}
.spread{position:absolute;top:150px;display:flex;height:600px;box-shadow:0 18px 40px rgba(0,0,0,.18)}
.spread--outside{left:30px}
.spread--inside{left:630px}
.panel{position:relative;width:270px;height:600px;overflow:hidden}
.photo{position:absolute;background:linear-gradient(135deg,#f2efec,#cfc7c0 60%,#b9aea6)}
.ornament{position:absolute;background:linear-gradient(180deg,rgba(235,235,235,.35),rgba(110,110,110,.35));border-radius:40px}

/* welcome panel */
.welcome{background:var(--footer)}
.welcome__photo{left:0;top:14px;width:270px;height:244px;background:radial-gradient(circle at 70% 45%,#e9a06a 0,#d9b6a0 18%,#efe9e4 45%,#f7f6f5 80%)}
.welcome__body{position:absolute;left:0;top:258px;width:270px;height:294px;background:var(--panel-dark);text-align:center;padding-top:12px;font-family:"Nunito",sans-serif}
.welcome__line{font-size:15px;font-weight:600;letter-spacing:.5px;line-height:1.45}
.welcome__hello{font-size:22px;color:var(--accent-green);letter-spacing:1px;margin:2px 0}
.badges{display:flex;justify-content:space-around;align-items:center;margin:18px 30px 0}
.badge-square{width:52px;height:76px;background:#f4f4f4;border:3px solid #2a3b8c}
.badge-circle{width:64px;height:64px;border-radius:50%;background:#fff;border:3px solid #2c8ac9}
.welcome__name{margin-top:20px;font-size:15px;font-weight:700;font-family:"Montserrat",sans-serif}
.welcome__footer{position:absolute;left:0;bottom:0;width:270px;height:48px;display:flex;align-items:center;justify-content:space-around;color:#333;font-size:11px;font-style:italic;padding:0 10px}
.contact{display:flex;align-items:center;gap:6px;line-height:1.25}

/* cover panel */
.cover{background:var(--panel)}
.brand{position:absolute;left:16px;top:16px;display:flex;align-items:center;gap:10px}
.brand__mark{width:40px;height:40px;border-radius:50%;background:#fff}
.brand__text{text-align:right;font-size:14px;line-height:1.15}
.brand__role{display:block;font-size:11px}
.cover__title{position:absolute;left:0;width:270px;top:84px;text-align:center;font-size:19px;font-weight:400}
.vertical{position:absolute;right:26px;top:138px;display:flex;flex-direction:column;align-items:center;font-size:18px;font-weight:500;line-height:24.5px}
.frame{position:absolute;left:48px;top:196px;width:86px;height:104px;background:#5e5e5e;border-radius:8px}
.frame .photo{left:6px;top:8px;width:76px;height:88px;border-radius:4px}
.cover__ornament{left:132px;top:170px;width:60px;height:250px}
.cover__date{position:absolute;left:18px;top:444px;font-size:21px;font-weight:700;text-shadow:1px 2px 2px rgba(0,0,0,.35)}
.cover__arrow{position:absolute;left:196px;top:432px}
.cover__box{position:absolute;left:0;top:494px;width:200px;height:66px;background:var(--panel-dark);border-radius:0 14px 14px 0;text-align:center;font-size:12px;line-height:1.3;padding-top:6px}
.cover__texture{position:absolute;left:208px;top:486px;width:56px;height:74px;background:rgba(220,220,220,.18)}
.cover__footer{position:absolute;left:0;bottom:0;width:270px;height:40px;background:var(--footer);color:var(--footer-ink);font-size:9px;font-style:italic;letter-spacing:.6px;display:flex;align-items:center;justify-content:center}

/* treatment panel */
.treatment{background:var(--panel-mid);border-right:1px solid #9a9a9a;text-align:center}
.treatment__heading{margin-top:26px;font-size:15px;font-weight:700;letter-spacing:5px}
.treatment__intro{margin-top:10px;font-size:11.5px;line-height:1.45;letter-spacing:.4px}
.treatment__examples{margin-top:10px;font-size:9px;line-height:1.4;letter-spacing:.8px}
.photo-frame{position:absolute;background:#c6c6c6}
.photo-frame--large{left:34px;top:248px;width:210px;height:170px;padding:7px}
.photo-frame--small{left:10px;top:352px;width:104px;height:116px;background:#555;padding:0 6px 6px 0}
.photo-frame .photo{position:static;width:100%;height:100%}
.photo--neck{background:linear-gradient(135deg,#f4eee9,#e3cfc0 55%,#7a5c4b)}
.photo--room{background:linear-gradient(160deg,#f3f5f6,#c9d7df 50%,#7fa6c2)}
.treatment__ornament{left:170px;top:428px;width:44px;height:92px;border-radius:22px}
.treatment__focus{position:absolute;left:0;bottom:26px;width:270px;font-size:17px;font-weight:500}
.treatment__focus small{display:block;font-size:9px;margin-top:3px}

/* offers panel */
.offers{background:#7e7e7e;text-align:center;padding:0 12px}
.offers__heading{margin-top:26px;font-size:16px;font-weight:700;line-height:1.45;letter-spacing:.5px;font-family:"Nunito",sans-serif}
.offers__list{list-style:none;margin-top:18px;font-family:"Nunito",sans-serif}
.offers__item{font-size:14px;font-weight:600;margin-bottom:19px;line-height:1.3}
.offers__item small{display:block;font-size:8px;font-weight:400}
.offers__ornament{left:112px;top:532px;width:46px;height:30px;border-radius:50%;background:rgba(255,255,255,.85)}
</style>
</head>
<body>

<section class="spread spread--outside">
  <article class="panel welcome">
    <div class="photo welcome__photo" role="img" aria-label="Foto: Person fasst sich an den schmerzenden Nacken"></div>
    <div class="welcome__body">
      <p class="welcome__line">Ab dem 17.04.2023<br>heiße ich Sie</p>
      <p class="welcome__hello">Herzlich Willkommen</p>
      <p class="welcome__line">in meiner neuen Praxis</p>
      <div class="badges">
        <div class="badge-square" role="img" aria-label="Zertifikat"></div>
        <div class="badge-circle" role="img" aria-label="Verbandsmitgliedschaft"></div>
      </div>
      <p class="welcome__name">Torben Lux</p>
    </div>
    <div class="welcome__footer">
      <div class="contact">
        <svg width="16" height="22" viewBox="0 0 16 22"><path d="M8 1a6.5 6.5 0 0 0-6.5 6.5C1.5 12.5 8 20 8 20s6.5-7.5 6.5-12.5A6.5 6.5 0 0 0 8 1z" fill="none" stroke="#333" stroke-width="1.3"/><circle cx="8" cy="7.5" r="2.4" fill="none" stroke="#333" stroke-width="1.3"/></svg>
        <span>Lindenweg 7<br>57312 Kirchen</span>
      </div>
      <div class="contact">
        <svg width="18" height="18" viewBox="0 0 24 24"><path d="M6.6 10.8a15 15 0 0 0 6.6 6.6l2.2-2.2a1 1 0 0 1 1-.25 11.4 11.4 0 0 0 3.6.57 1 1 0 0 1 1 1V20a1 1 0 0 1-1 1A17 17 0 0 1 3 4a1 1 0 0 1 1-1h3.5a1 1 0 0 1 1 1c0 1.25.2 2.45.57 3.57a1 1 0 0 1-.25 1z" fill="none" stroke="#333" stroke-width="1.4"/></svg>
        <span>02741/73945</span>
      </div>
    </div>
  </article>

  <article class="panel cover">
    <div class="brand">
      <span class="brand__mark"></span>
      <p class="brand__text">Torben Lux<span class="brand__role">Heilpraktiker</span></p>
    </div>
    <h1 class="cover__title">Natur- und Chiropraxis</h1>
    <div class="vertical" aria-label="Neueröffnung">
      <span>N</span><span>E</span><span>U</span><span>E</span><span>R</span><span>Ö</span><span>F</span><span>F</span><span>N</span><span>U</span><span>N</span><span>G</span>
    </div>
    <div class="frame"><div class="photo" role="img" aria-label="Foto: Therapeut behandelt einen Ellenbogen"></div></div>
    <div class="ornament cover__ornament" role="img" aria-label="Dekorative Wirbelsäulen-Grafik"></div>
    <p class="cover__date">17.APRIL 2023</p>
    <svg class="cover__arrow" width="60" height="56" viewBox="0 0 60 56">
      <path d="M48 6 C58 40 30 52 10 26" fill="none" stroke="#555" stroke-width="4" stroke-linecap="round"/>
      <path d="M8 38 L8 24 L22 26" fill="none" stroke="#555" stroke-width="4" stroke-linecap="round" stroke-linejoin="round"/>
    </svg>
    <div class="cover__box">Ganzheitliche Chiropraktik<br>und<br>manuelle Gelenktherapie.</div>
    <div class="cover__texture" role="img" aria-label="Dekoratives Punktraster"></div>
    <p class="cover__footer">Die Leistungsangebote finden Sie im Innenteil</p>
  </article>
</section>

<section class="spread spread--inside">
  <article class="panel treatment">
    <h2 class="treatment__heading">BEHANDLUNG VON</h2>
    <p class="treatment__intro">Patienten mit<br>chronischen oder akuten<br>Beschwerden des<br>Halte- und Bewegungsapparates</p>
    <p class="treatment__examples">(z.b.Migräne+Spannungskopfschmerzen,<br>Muskelkettendysbalancen,<br>Bandscheibenvorfälle)</p>
    <div class="photo-frame photo-frame--large"><div class="photo photo--neck" role="img" aria-label="Foto: Hand auf dem Nacken einer Patientin mit angedeuteter Wirbelsäule"></div></div>
    <div class="photo-frame photo-frame--small"><div class="photo photo--room" role="img" aria-label="Foto: Patientin sitzt im Behandlungsraum und hält sich den Rücken"></div></div>
    <div class="ornament treatment__ornament" role="img" aria-label="Dekorative Wirbelsäulen-Grafik"></div>
    <p class="treatment__focus">HWS und Atlastherapie<small>(Bei Tinnitus, Schwindel, Kopfschmerzen)</small></p>
  </article>

  <article class="panel offers">
    <h2 class="offers__heading">UNSERE<br>THERAPIEANGEBOTE</h2>
    <ul class="offers__list">
      <li class="offers__item">Naturheilkunde<br>und Vitalstoffinfusionen<small>(Bei LongCovid, chronischem Erschöpfungssyndrom)</small></li>
      <li class="offers__item">Neuraltherapie</li>
      <li class="offers__item">Extensionstherapie</li>
      <li class="offers__item">Wärmetherapie</li>
      <li class="offers__item">Magnetfeldtherapie</li>
      <li class="offers__item">biologische Arthrosebehandlung</li>
      <li class="offers__item">Dry-Needling Therapie</li>
      <li class="offers__item">Extrakorporale Stoßwellentherapie<small>( Bei Fersensporn, Kalkschulter, Sehnenansatzentzündungen.)</small></li>
    </ul>
    <div class="ornament offers__ornament" role="img" aria-label="Dekoratives Lotusblüten-Symbol"></div>
  </article>
</section>

</body>
</html>
```